Business Stationery Design

I would like to get some stationery designed for my company. The stationery should include a letterhead, envelope, and business card. We are a technology consulting company specializing in Healthcare IT, and Education management systems. The colors of the stationery should match the logo. The logo is uploaded.

Target Market(s)

Hospitals, Clinics. Doctors offices. Private Schools.

Industry/Entity Type

Business

```html
<!DOCTYPE html>
<html lang="en">
<head>
<meta charset="utf-8">
<title>Clearmont Advisory Group – Business Cards</title>
<link rel="stylesheet" href="https://fonts.googleapis.com/css2?family=Quicksand:wght@500;600&display=swap">
<style>
  :root {
    --backdrop: #f8d569;
    --card-cream: #fbf1c9;
    --leaf-green: #76bd34;
    --sun-orange: #f4b41a;
    --line-white: #ffffff;
    --card-edge: #b8952a;
  }
  html, body {
    margin: 0;
    padding: 0;
    width: 1200px;
    height: 1200px;
    overflow: hidden;
    background: var(--backdrop);
    font-family: "Quicksand", sans-serif;
  }
  .canvas {
    position: relative;
    width: 1200px;
    height: 1200px;
  }
  .card {
    position: absolute;
    top: 496px;
    width: 336px;
    height: 204px;
    background: var(--card-cream);
    outline: 2px solid var(--card-edge);
    overflow: hidden;
  }
  .card--front { left: 280px; }
  .card--back { left: 656px; }
  .card__shapes {
    position: absolute;
    inset: 0;
    width: 336px;
    height: 204px;
  }
  .brand {
    position: absolute;
    display: flex;
    flex-direction: column;
    align-items: center;
  }
  .brand__mark {
    border-radius: 50%;
    background: var(--sun-orange);
  }
  .brand__name {
    margin: 6px 0 0;
    color: var(--leaf-green);
    font-weight: 600;
    text-align: center;
    line-height: 1.05;
  }
  .card--front .brand { left: 84px; top: 36px; width: 170px; }
  .card--front .brand__mark { width: 58px; height: 58px; }
  .card--front .brand__name { font-size: 22px; }
  .card--back .brand { left: 16px; top: 36px; width: 120px; }
  .card--back .brand__mark { width: 46px; height: 46px; }
  .card--back .brand__name { font-size: 17px; }
  .faint-mark {
    position: absolute;
    left: 190px;
    top: 30px;
    width: 120px;
    height: 120px;
    border-radius: 50%;
    background: var(--leaf-green);
    opacity: 0.12;
  }
  .contact {
    position: absolute;
    right: 16px;
    top: 52px;
    text-align: right;
    color: var(--leaf-green);
    font-weight: 500;
    font-size: 9.5px;
    line-height: 11.5px;
  }
  .contact__name { font-size: 15px; line-height: 16px; font-weight: 500; }
  .contact__gap { height: 10px; }
  .contact p { margin: 0; }
</style>
</head>
<body>
<main class="canvas">

  <section class="card card--front" aria-label="Business card front">
    <svg class="card__shapes" viewBox="0 0 280 170" preserveAspectRatio="none" aria-hidden="true">
      <path d="M165 0 Q235 8 280 24 L280 0 Z" fill="var(--leaf-green)"/>
      <path d="M160 2 Q232 10 280 27" fill="none" stroke="var(--line-white)" stroke-width="1.2"/>
      <path d="M0 126 Q140 160 280 150 L280 170 L0 170 Z" fill="var(--leaf-green)"/>
      <path d="M0 131 Q140 164 280 154" fill="none" stroke="var(--line-white)" stroke-width="1.2"/>
    </svg>
    <div class="faint-mark" role="img" aria-label="Faint brand emblem decoration"></div>
    <div class="brand">
      <div class="brand__mark"></div>
      <p class="brand__name">Clearmont<br>Advisory Group</p>
    </div>
  </section>

  <section class="card card--back" aria-label="Business card back">
    <svg class="card__shapes" viewBox="0 0 280 170" preserveAspectRatio="none" aria-hidden="true">
      <path d="M165 0 Q235 8 280 24 L280 0 Z" fill="var(--leaf-green)"/>
      <path d="M160 2 Q232 10 280 27" fill="none" stroke="var(--line-white)" stroke-width="1.2"/>
      <path d="M0 126 Q140 160 280 150 L280 170 L0 170 Z" fill="var(--leaf-green)"/>
      <path d="M0 131 Q140 164 280 154" fill="none" stroke="var(--line-white)" stroke-width="1.2"/>
    </svg>
    <div class="brand">
      <div class="brand__mark"></div>
      <p class="brand__name">Clearmont<br>Advisory Group</p>
    </div>
    <div class="contact">
      <p class="contact__name">Your Name</p>
      <p>CEO / President</p>
      <p>info@yourbusiness.com</p>
      <div class="contact__gap"></div>
      <p>Full Address, FA 01</p>
      <p>City Country</p>
      <p>0123 456 789</p>
      <p>www.yourbusiness.com</p>
    </div>
  </section>

</main>
</body>
</html>
```